依頼詳細
化粧水 パッケージデザイン
箱無し
シンプルかつ高級感のあるデザイン
ミレニアム世代、50代、60代をメインとし販売
自社ハーブ畑で撮影した写真
(カモミール)を使用していただき、こちら写真をメインとし
ロゴ、ネーミングの配置
全体的なイメージのデザインを依頼いたします。

記載項目
・大きさ:縦108mm×140mm
・化粧品表示のルールで、文字の大きさは7ポイント以上、 ・プラマークの大きさは高さを6mm以上にしてください。 ・円柱の容器に1枚のシールをぐるっと巻きつけて貼る形になります。

ラミネート加工
カラーはパール入りデザイン希望

金文字で、ブランド名
『VELMIRAE』記載希望
希望イメージ
シンプル 複雑
単色 カラフル
暗い 明るい
日常 高級
遊び心 厳粛
未来的 伝統的
女性的 男性的
希望する色
赤系、水色系、黄・オレンジ系、追加、ホワイトパール系のカラー
■ 選んだ理由

自社のハーブ素材を生かし、+アルファの工夫があり好感度を持てた。シンプルな上に必要な情報が記載されて良い。

■ 提案者全員のお礼・コメント

多くのご提案、誠にありがとうございました。また、自社製品を作成していく上でお力添えをいただく事もあると思います、何卒よろしくお願い申し上げます。

```html
<!DOCTYPE html>
<html lang="en">
<head>
<meta charset="utf-8">
<title>VELMIRAE Herbal Mist Spray Label</title>
<link rel="stylesheet" href="https://fonts.googleapis.com/css2?family=Bodoni+Moda:wght@400;500&family=Lato:wght@300;400&display=swap">
<style>
  :root {
    --backdrop: #f4f4f2;
    --label-cream: #efece2;
    --label-top: #ebeadf;
    --gold: #b39556;
    --gold-light: #d2bb86;
    --ink-soft: #6f6a60;
    --ring: #8d887e;
    --photo-light: #c9cdb4;
    --photo-mid: #8e9d6a;
    --photo-deep: #5d7040;
  }
  * { margin: 0; padding: 0; box-sizing: border-box; }
  html, body {
    width: 1200px;
    height: 2180px;
    overflow: hidden;
    background: var(--backdrop);
  }
  .label {
    position: absolute;
    left: 120px;
    top: 120px;
    width: 960px;
    height: 1940px;
    background: linear-gradient(180deg, var(--label-top) 0%, var(--label-cream) 12%, var(--label-cream) 100%);
    overflow: hidden;
    box-shadow: 0 2px 18px rgba(0,0,0,0.06);
  }
  .gold-rule {
    position: absolute;
    left: 0;
    width: 100%;
    background: var(--gold);
  }
  .gold-rule--main { top: 110px; height: 5px; background: linear-gradient(90deg, var(--gold) 0%, var(--gold-light) 50%, var(--gold) 100%); }
  .gold-rule--thin { top: 122px; height: 2px; opacity: 0.6; }
  .product-type {
    position: absolute;
    top: 296px;
    width: 100%;
    text-align: center;
    font-family: "Lato", sans-serif;
    font-weight: 400;
    font-size: 52px;
    letter-spacing: 1px;
    color: var(--ink-soft);
  }
  .brand-name {
    position: absolute;
    top: 470px;
    width: 100%;
    text-align: center;
    font-family: "Bodoni Moda", serif;
    font-weight: 500;
    font-size: 100px;
    line-height: 1;
    letter-spacing: 30px;
    padding-left: 30px;
    color: var(--gold);
  }
  .ingredient {
    position: absolute;
    left: 50%;
    transform: translateX(-50%);
    border: 2px solid var(--ring);
    border-radius: 50%;
    display: flex;
    align-items: center;
    justify-content: center;
    text-align: center;
    font-family: "Lato", sans-serif;
    font-weight: 400;
    color: var(--ink-soft);
  }
  .ingredient--nmn { top: 700px; width: 260px; height: 260px; font-size: 44px; letter-spacing: 1px; }
  .ingredient--stem { top: 1050px; width: 300px; height: 300px; font-size: 38px; line-height: 1.25; }
  .cross {
    position: absolute;
    top: 965px;
    width: 100%;
    text-align: center;
    font-family: "Lato", sans-serif;
    font-weight: 300;
    font-size: 64px;
    line-height: 80px;
    color: var(--ink-soft);
  }
  .chamomile-photo {
    position: absolute;
    left: 0;
    top: 1470px;
    width: 100%;
    height: 470px;
    background: linear-gradient(165deg, var(--photo-light) 0%, var(--photo-mid) 50%, var(--photo-deep) 100%);
  }
</style>
</head>
<body>
  <main class="label">
    <div class="gold-rule gold-rule--main"></div>
    <div class="gold-rule gold-rule--thin"></div>

    <p class="product-type">Herbal Mist Spray</p>
    <h1 class="brand-name">VELMIRAE</h1>

    <div class="ingredient ingredient--nmn">NMN</div>
    <div class="cross">×</div>
    <div class="ingredient ingredient--stem">Human<br>stem cell<br>extract</div>

    <div class="chamomile-photo" role="img" aria-label="Photograph of chamomile flowers in the herb field"></div>
  </main>
</body>
</html>
```